Corporate Branding - Web and Print

A UK based company will like to use an existing logo to create branding materials for all marketing related documents, including business card, prints, letterhead, Website, Twitter, Facebook, Instagram logo etc. This company serves high-end clientele in the fashion, health and wellness and as such high quality and class is of utmost importance.
Where the logo can be modernised without losing its character then experiment. The main thing is to have a corporate branding which can be used later for brochures, Business Plan infographics.
The prominent colour within the organisation is burnt orange with no secondary colour. However if you believe a secondary colour is needed then use it, otherwise keep it simple and classy. Any chosen colours have to match perfectly.
Target Market(s)
High net worth individuals
Industry/Entity Type
Health And Wellness
Contact Information for Business Card
classy
Look and feel
Each slider illustrates characteristics of the customer's brand and the style your logo design should communicate.

```html
<!DOCTYPE html>
<html lang="en">
<head>
<meta charset="utf-8">
<title>Velora Business Card</title>
<link rel="stylesheet" href="https://fonts.googleapis.com/css2?family=Oswald:wght@500;600&family=Work+Sans:wght@400;500&display=swap">
<style>
  :root {
    --burnt-orange: #f28a1c;
    --orange-light: #f9a82a;
    --card-white: #ffffff;
    --ink: #555555;
    --backdrop: #1c1c1c;
  }
  * { margin: 0; padding: 0; box-sizing: border-box; }
  html, body { width: 1200px; height: 1000px; overflow: hidden; }
  body {
    background: var(--backdrop);
    position: relative;
    font-family: "Work Sans", sans-serif;
  }
  .card {
    position: absolute;
    width: 540px;
    height: 310px;
    border-radius: 30px;
    box-shadow: 0 18px 40px rgba(0,0,0,0.5);
  }
  .card-front {
    left: 90px;
    top: 170px;
    background: linear-gradient(135deg, var(--burnt-orange), var(--orange-light));
    display: flex;
    align-items: center;
    justify-content: center;
  }
  .card-back {
    left: 570px;
    top: 520px;
    background: var(--card-white);
  }
  .brand {
    display: flex;
    align-items: center;
    gap: 14px;
    font-family: "Oswald", sans-serif;
    font-weight: 600;
    letter-spacing: 2px;
  }
  .brand-dot {
    width: 34px;
    height: 34px;
    border-radius: 50%;
  }
  .card-front .brand { color: var(--card-white); font-size: 58px; }
  .card-front .brand-dot { background: var(--card-white); }
  .card-back .brand {
    position: absolute;
    left: 40px;
    top: 150px;
    color: var(--burnt-orange);
    font-size: 46px;
  }
  .card-back .brand-dot { background: var(--burnt-orange); width: 28px; height: 28px; }
  .contact-block {
    position: absolute;
    left: 300px;
    top: 52px;
  }
  .identity {
    border-left: 3px solid var(--burnt-orange);
    padding-left: 14px;
  }
  .person-name {
    font-family: "Oswald", sans-serif;
    font-weight: 600;
    color: var(--burnt-orange);
    font-size: 22px;
    letter-spacing: 0.5px;
  }
  .person-title { font-size: 14px; color: var(--ink); font-weight: 500; }
  .details {
    margin-top: 16px;
    border-left: 2px solid var(--burnt-orange);
    padding-left: 14px;
    font-size: 13px;
    color: var(--ink);
    line-height: 1.5;
  }
  .address { margin-bottom: 6px; }
  .detail-row { display: flex; align-items: center; gap: 8px; }
  .detail-row svg { width: 11px; height: 11px; fill: var(--burnt-orange); flex: none; }
  .accent { color: var(--burnt-orange); }
</style>
</head>
<body>
  <div class="card card-front">
    <div class="brand"><span class="brand-dot"></span>VELORA</div>
  </div>

  <div class="card card-back">
    <div class="brand"><span class="brand-dot"></span>VELORA</div>
    <div class="contact-block">
      <div class="identity">
        <p class="person-name">ADRIAN HALE</p>
        <p class="person-title">President</p>
      </div>
      <div class="details">
        <p class="address">Your Street Address,<br>Suite-111, State, Country</p>
        <p class="detail-row">
          <svg viewBox="0 0 24 24"><path d="M6.6 10.8a15.1 15.1 0 0 0 6.6 6.6l2.2-2.2a1 1 0 0 1 1-.25 11.4 11.4 0 0 0 3.6.6 1 1 0 0 1 1 1V20a1 1 0 0 1-1 1A17 17 0 0 1 3 4a1 1 0 0 1 1-1h3.5a1 1 0 0 1 1 1c0 1.25.2 2.45.6 3.6a1 1 0 0 1-.25 1z"/></svg>
          000 000 0000
        </p>
        <p class="detail-row">
          <svg viewBox="0 0 24 24"><path d="M2 5h20v14H2zm2 2v.5l8 5 8-5V7l-8 5z"/></svg>
          info@adrianhale.com
        </p>
        <p class="detail-row">
          <svg viewBox="0 0 24 24"><circle cx="12" cy="12" r="10"/></svg>
          www.<span class="accent">velora</span>.com
        </p>
      </div>
    </div>
  </div>
</body>
</html>
```